"leading industry company in search of a new web page"

we are searching for a clean, industry driven, engineered oriented web page design,

it need to be clean, and it need to have the chiefs company photo on the first page.
we are a mexican engineered company, we have 3 special sector specialties so in the front page we need to have a link to each one of these, and another one for CV "jobs" IM PUTING A COUPLE OD DESIGN IDEAL WITH OUR INFO SO YOU CAN PUT IT ALL TOGETHER

IM PUTING OUR LOGO AVAILABLE SO YOU CAN PUT IT IN THE PAGE

OUR WEB PAGE IS http://dravol.com.mx

Target Market(s)

INDUSTRY LIKES ENERGY AND PETROL
COMPANIES IN THE ENGINEERING BUSINESS

Industry/Entity Type

Industry

Requirements
Must have
• CLEAN DESIGN,
• HIRING AND CV DEDICATED MENU TAB
• THE 3 DIVISIONS OF THE COMPANY
• SOCIAL MEDIA ON THE BOTTOM "JUST PLAIN CIRCLE AND PLAIN CIRCLE"
Nice to have
• COHERENCE WITH THE LOGO COLORS

```html
<!DOCTYPE html>
<html lang="en">
<head>
<meta charset="utf-8">
<title>Dravol – Quality Engineering Consulting</title>
<link href="https://fonts.googleapis.com/css2?family=Ubuntu:wght@400;500;700&family=Noto+Sans:wght@400;700&display=swap" rel="stylesheet">
<style>
:root{
  --green:#2f9a2a; --green-dark:#0f6e12; --green-light:#3fb53a;
  --red:#e0283d; --red-dark:#c41d30; --red-light:#ee6a6a;
  --ink:#222; --muted:#555; --page:#f1f1f1; --white:#fff;
  --footer:#2b2c30; --footer-line:#3a3b40;
}
*{margin:0;padding:0;box-sizing:border-box}
html,body{width:1152px;height:1200px;overflow:hidden}
body{position:relative;background:var(--page);font-family:"Noto Sans",sans-serif;color:var(--ink)}
.abs{position:absolute}
.header{left:103px;top:0;width:947px;height:108px;background:var(--white)}
.page-bg-top{left:0;top:0;width:1152px;height:108px;background:var(--white)}
.brand{left:12px;top:22px;display:flex;align-items:center;gap:10px;font-family:"Ubuntu",sans-serif;font-weight:500;font-size:44px;color:var(--red)}
.brand .dot{width:60px;height:60px;border-radius:50%;background:var(--green)}
.social{right:0;top:5px;display:flex;gap:7px}
.social span{width:27px;height:27px;border-radius:50%;background:#3b7fd6;display:block}
.social span+span{background:#2aa3e6}
.contact-today{right:10px;top:50px;font-family:"Ubuntu",sans-serif;color:var(--green);font-size:16px}
.phone{right:10px;top:70px;display:flex;align-items:center;gap:6px;font-family:"Ubuntu",sans-serif;font-weight:500;font-size:24px;color:#333}
.hero{left:0;top:108px;width:1152px;height:412px;background:linear-gradient(180deg,#3a3a3a 0%,#8c8c8c 45%,#6b6b6b 75%,#2f2f2f 100%)}
.nav{left:103px;top:108px;width:947px;height:44px;background:linear-gradient(#3fae35,#167a16);display:flex;align-items:center;font-family:"Ubuntu",sans-serif;font-size:14px;color:var(--white);box-shadow:0 2px 4px rgba(0,0,0,.4)}
.nav a{color:var(--white);text-decoration:none;text-align:center;border-right:1px solid rgba(255,255,255,.25);line-height:22px}
.nav a:last-child{border-right:none}
.nav .active{background:var(--green-dark);border-radius:12px;padding:0 16px;border:1px solid #5bc655;margin-right:21px}
.tagline{left:105px;top:243px;width:393px;height:153px;background:rgba(20,20,20,.72);padding:4px 5px;font-family:"Ubuntu",sans-serif;font-weight:700;font-size:27px;line-height:29px;color:var(--white)}
.tagline .co1{color:var(--red)} .tagline .co2{color:#8fd12c}
.slider-tab{left:518px;top:453px;width:120px;height:36px;background:#eee;border-radius:30px 30px 0 0;display:flex;justify-content:center;align-items:center;gap:6px}
.slider-tab i{width:13px;height:13px;border-radius:50%;background:#b9c6cf;display:block}
.slider-tab i.on{background:var(--green)}
.divisions{left:101px;top:486px;width:950px;height:68px;background:var(--white);box-shadow:0 12px 14px -10px rgba(0,0,0,.4)}
.division{top:8px;width:228px;height:51px;background:linear-gradient(#ef7a6c,#d92436);display:flex;align-items:center;gap:10px;padding-left:9px;font-family:"Ubuntu",sans-serif;color:var(--white);line-height:19px}
.division .ico{width:30px;height:30px;border-radius:50%;background:var(--white);opacity:.9;flex:none}
.division b{font-size:19px;display:block}
.division span{font-size:16px}
.section-title{display:flex;align-items:center;gap:6px;font-family:"Ubuntu",sans-serif;font-size:19px;color:#333;padding-bottom:10px;border-bottom:1px solid #ddd}
.section-title .ico{width:30px;height:30px;border-radius:50%;background:var(--red);flex:none}
.section-title .name{color:var(--red);font-weight:500;font-size:24px}
.section-title em{font-style:normal;color:var(--red);font-weight:500}
.welcome{left:101px;top:590px;width:560px}
.welcome p{font-size:12.5px;line-height:17.3px;text-align:justify;margin:14px 5px 0;letter-spacing:.2px}
.welcome p+p{margin-top:17px}
.btn{display:inline-block;background:var(--red);color:var(--white);font-size:11.5px;font-family:"Ubuntu",sans-serif;padding:2px 9px;border-radius:3px}
.news{left:706px;top:590px;width:343px}
.news-item{margin-left:9px;font-size:12.3px;line-height:15px;padding:12px 0 14px}
.news-item+.news-item{border-top:1px dotted #777;padding-top:16px}
.news-date{font-weight:700;font-family:"Ubuntu",sans-serif;font-size:13px;display:flex;align-items:center;gap:7px;margin-bottom:4px}
.news-date i{width:13px;height:13px;border:2px solid var(--red);display:block}
.partners-tab{left:480px;top:879px;width:192px;height:36px;background:#e4e4e4;border-radius:40px 40px 0 0;text-align:center;font-family:"Ubuntu",sans-serif;font-size:19px;color:#333;line-height:44px}
.partners-tab em{font-style:normal;color:var(--red);font-weight:500}
.partners{left:0;top:912px;width:1152px;height:122px;background:repeating-linear-gradient(135deg,#e2e2e2 0 2px,#ececec 2px 4px)}
.arrow{top:45px;width:38px;height:38px;border-radius:50%;background:#111;box-shadow:0 0 0 3px #ddd}
.partner-row{left:193px;top:42px;display:flex;gap:15px;align-items:center}
.partner-row i{display:block;background:#444;opacity:.85}
.footer{left:0;top:1034px;width:1152px;height:161px;background:var(--footer)}
.footer-bar{left:0;top:1195px;width:1152px;height:5px;background:var(--red)}
.footer h3{font-family:"Ubuntu",sans-serif;font-size:17px;color:var(--red);font-weight:700;margin-bottom:9px}
.footer ul{list-style:none;font-size:12.5px;color:#e8e8e8;line-height:24px}
.footer .cols{display:flex;gap:48px}
.footer .addr{font-size:12.5px;color:#e8e8e8;line-height:17.5px}
.footer table{font-size:12.5px;color:#e8e8e8;border-collapse:collapse}
.footer td{padding:0 6px 8px 0}
.footer-brand{left:837px;top:40px;display:flex;align-items:center;gap:6px;font-family:"Ubuntu",sans-serif;font-size:44px;font-weight:500;color:var(--white)}
.footer-brand .dot{width:58px;height:58px;border-radius:50%;background:var(--white)}
.copyright{left:845px;top:120px;font-size:12.5px;color:#e8e8e8}
</style>
</head>
<body>
<div class="abs page-bg-top"></div>
<header class="abs header">
  <div class="abs brand"><span class="dot"></span>dravol</div>
  <div class="abs social" aria-label="Social media"><span></span><span></span></div>
  <div class="abs contact-today">Contact Us Today!</div>
  <div class="abs phone">
    <svg width="24" height="24" viewBox="0 0 24 24"><circle cx="12" cy="12" r="11" fill="none" stroke="#333" stroke-width="1.6"/><path d="M9 6c-2 1-2 3-1 6s3 5 5 6c1 .5 2 0 2.5-1l-2-2-1.3.8c-1-.6-2-2-2.5-3.5l1.2-1L10 6z" fill="#333"/></svg>
    +52 (55) 5140 2287
  </div>
</header>

<div class="abs hero" role="img" aria-label="Black and white photograph of an industrial refinery at night with steam rising"></div>

<nav class="abs nav">
  <a style="margin-left:52px" class="active">HOME</a>
  <a style="width:152px">ABOUT US</a>
  <a style="width:152px">SOLUTIONS</a>
  <a style="width:139px">SERVICES</a>
  <a style="width:178px">TECHNOLOGIES</a>
  <a style="width:160px">CONTACT US</a>
</nav>

<div class="abs tagline"><span class="co1">DRA</span><span class="co2">VOL</span> provides premier consulting services for quality engineering in the nuclear, industrial and construction fields.</div>

<div class="abs slider-tab"><i></i><i class="on"></i><i></i><i></i></div>

<section class="abs divisions">
  <a class="abs division" style="left:8px"><span class="ico"></span><div><b>INDUSTRIAL</b><span>DIVISION</span></div></a>
  <a class="abs division" style="left:243px"><span class="ico"></span><div><b>VERIFICATION</b><span>DIVISION</span></div></a>
  <a class="abs division" style="left:478px"><span class="ico"></span><div><b>ADMINISTRATION</b><span>DIVISION</span></div></a>
  <a class="abs division" style="left:714px"><span class="ico"></span><div><b>WE ARE HIRING</b><span>SEND YOUR CV</span></div></a>
</section>

<section class="abs welcome">
  <h2 class="section-title"><span class="ico"></span>Welcome to <span class="name">dravol</span></h2>
  <p>DRAVOL since its founding in 1981 has been active in the field of quality engineering, materials, welding, and industrial equipment, technical assistance to metallurgical problems in general as well as the verification of compliance with official Mexican norms and standards Mexican.</p>
  <p>In 1986 DRAVOL joins Punta Arena nuclear power project of the National Power Board as a specialized and skilled work to develop quality control, technical advice and consultancy. This participation in the nuclear field...</p>
  <a class="btn" style="margin-top:18px">Read More</a>
</section>

<section class="abs news">
  <h2 class="section-title"><span class="ico"></span>Latest <em>News</em></h2>
  <div class="news-item"><div class="news-date"><i></i>10-10-2013</div>Lorem ipsum dolor sit amet, consectetur adipisicing elit sed do eiusmod.</div>
  <div class="news-item"><div class="news-date"><i></i>10-09-2013</div>Lorem ipsum dolor sit amet, consectetur adipisicing elit sed do eiusmod.</div>
  <a class="btn" style="margin:2px 0 0 9px">Read More</a>
</section>

<div class="abs partners-tab">Our <em>Partners</em></div>
<section class="abs partners" aria-label="Partners">
  <svg class="abs arrow" style="left:104px" viewBox="0 0 38 38"><path d="M22 11l-8 8 8 8" stroke="#fff" stroke-width="4" fill="none"/></svg>
  <svg class="abs arrow" style="left:1010px" viewBox="0 0 38 38"><path d="M16 11l8 8-8 8" stroke="#fff" stroke-width="4" fill="none"/></svg>
  <div class="abs partner-row">
    <i style="width:26px;height:38px"></i>
    <i style="width:32px;height:38px;border-radius:50%"></i>
    <i style="width:86px;height:22px;border-radius:11px"></i>
    <i style="width:28px;height:38px"></i>
    <i style="width:96px;height:24px"></i>
    <i style="width:42px;height:42px;border-radius:50%"></i>
    <i style="width:100px;height:18px"></i>
    <i style="width:38px;height:40px"></i>
    <i style="width:58px;height:36px"></i>
    <i style="width:66px;height:38px;border-radius:50%"></i>
    <i style="width:50px;height:34px"></i>
  </div>
</section>

<footer class="abs footer">
  <div class="abs" style="left:103px;top:28px">
    <h3>NAVIGATION</h3>
    <div class="cols">
      <ul><li>Home</li><li>About Us</li><li>Solutions</li><li>Services</li></ul>
      <ul><li>Technologies</li><li>Contact Us</li></ul>
    </div>
  </div>
  <div class="abs" style="left:332px;top:28px">
    <h3>CONTACT US</h3>
    <div class="addr" style="margin-top:6px">Av. Ingenieros 214<br>Col. Valle Norte 11620<br>México, D.F.<br>México</div>
  </div>
  <table class="abs" style="left:497px;top:63px">
    <tr><td>Phone</td><td>:</td><td>+52 (55) 5140 2287</td></tr>
    <tr><td>Fax</td><td>:</td><td>+52 (55) 5140 2290</td></tr>
    <tr><td>Email</td><td>:</td><td>info@dravol.com.mx</td></tr>
  </table>
  <div class="abs footer-brand"><span class="dot"></span>dravol</div>
  <div class="abs copyright">© 2013, Dravol. All rights reserved.</div>
</footer>
<div class="abs footer-bar"></div>
</body>
</html>
```